Beautiful, sharp, website design for family-run property development company.

We are property developers in Kent (south east of London) who want to see the local town change. We are the only local property developer that is a family run business, focussing primarily on converting old, dilapidated Victorian buildings into beautiful residential spaces. Unlike other national developers, we work to regenerate buildings to create new employment opportunities, housing, and revive the town Centre .

Target Market(s)

1. Investors and Joint Venture partners - people with money to invest in property
2. Buyers of property - 25 to 40 year old, young professionals.
3. Commercial funders (people lending money to our projects
4. Professional team: Architects, builders, Estate agent who want to work with us

Industry/Entity Type

Real Estate Development

Coding

Number of Pages Required

Font styles to use
Other font styles liked:
• Please follow the brief of stylish, elegant, modern

Colors

Designer to choose colors to be used in the design.

Requirements
Must have
• Please use these websites as a reference of what we are looking to achieve.
• http://brellmoorhomes.com/#page5
• https://fernwick.co.uk/
• http://ambertide.co.uk/
• http://www.theharroweyestates.co.uk/about-harrowey
• Clean, simple, elegant, minimal design.
• Images of interiors of houses that have been converted from old buildings
• Images of farm buildings e.g. barns that have been converted to new homes or offices. Images of properties that may have been an old factory or old commercial property that is now a trendy apartment.
• Please use images of properties and interiors that are from the South East of England (including Kent, Surrey, Sussex, Hampshire, Dorset). There is a distinct style of housing in this part of England.
Nice to have
• Colours consistent with our brand colour palette (attached)

```html
<!DOCTYPE html>
<html lang="en">
<head>
<meta charset="utf-8">
<title>Quartz Oak – Property Developers</title>
<link href="https://fonts.googleapis.com/css2?family=Montserrat:wght@400;500;600;700&display=swap" rel="stylesheet">
<style>
:root{
  --ink:#1f2324;
  --dark:#2a2f30;
  --darker:#1c1f20;
  --white:#ffffff;
  --grey-text:#4a4f52;
  --accent:#4f6b78;
  --mint:#e9f1ea;
  --light:#f3f4f4;
}
*{box-sizing:border-box;margin:0;padding:0}
html,body{width:1200px;height:2744px;overflow:hidden}
body{font-family:"Montserrat",sans-serif;color:var(--ink);background:var(--white);position:relative}
.abs{position:absolute}

/* header + hero */
.hero{left:0;top:0;width:1200px;height:590px}
.hero-photo{position:absolute;inset:0;background:linear-gradient(100deg,#e7eaec 0%,#d6dadc 45%,#b9bfc2 70%,#e4e6e8 100%)}
.hero-fade{position:absolute;left:0;top:0;width:620px;height:590px;background:linear-gradient(90deg,rgba(255,255,255,.75),rgba(255,255,255,0))}
.site-header{position:absolute;left:0;top:0;width:1200px;height:125px;background:rgba(35,40,41,.92);display:flex;align-items:center;justify-content:center;gap:34px}
.nav-link{color:var(--white);font-size:20px;font-weight:600;letter-spacing:.5px;text-decoration:none}
.brand{display:flex;flex-direction:column;align-items:center;gap:6px;margin:0 36px}
.brand-mark{width:26px;height:26px;border:2px solid #8fb3b0}
.brand-name{color:#8fb3b0;font-size:15px;font-weight:600;letter-spacing:2px;text-transform:uppercase}
.hero-title{left:72px;top:210px;font-size:48px;font-weight:500;line-height:1.05;letter-spacing:1px}
.hero-title strong{display:block;font-weight:700;font-size:50px;letter-spacing:2px}
.hero-copy{left:72px;top:340px;width:470px;font-size:16px;line-height:1.35;color:var(--accent);font-weight:500}
.btn{display:inline-block;background:var(--dark);color:var(--white);font-size:15px;font-weight:600;padding:8px 22px;border-radius:20px}
.hero .btn{position:absolute;left:72px;top:432px}

/* services */
.services{left:0;top:640px;width:1200px;display:flex;justify-content:center;gap:120px}
.service{width:250px;text-align:center}
.service svg{width:130px;height:130px}
.service h3{margin-top:18px;font-size:19px;font-weight:700;letter-spacing:.5px;line-height:1.25}

/* motive */
.motive-band{left:0;top:1030px;width:1200px;height:172px;background:var(--dark)}
.motive-title{left:580px;top:1068px;color:var(--white);font-size:35px;font-weight:700;letter-spacing:2px}
.motive-rule{left:580px;top:1114px;width:560px;height:2px;background:var(--white)}
.motive-copy{left:580px;top:1128px;width:580px;color:var(--white);font-size:17px;line-height:1.35;font-weight:500}
.photo{position:absolute}
.photo-hall{left:118px;top:1005px;width:200px;height:340px;background:linear-gradient(160deg,#c48a55,#7a4a26);border:5px solid var(--white)}
.photo-lounge{left:225px;top:965px;width:250px;height:210px;background:linear-gradient(150deg,#2f4a3b,#7b6a4a);border:5px solid var(--white)}
.photo-dining{left:205px;top:1150px;width:210px;height:130px;background:linear-gradient(140deg,#9a6b3d,#d3b284);border:5px solid var(--white)}

/* developers */
.dev-title{left:80px;top:1430px;font-size:26px;font-weight:700;letter-spacing:1px;line-height:1.25}
.dev-title span{color:var(--accent)}
.dev-rule{left:80px;top:1500px;width:600px;height:2px;background:#9aa3a6}
.dev-copy{left:80px;top:1515px;width:560px;font-size:15px;line-height:1.45;color:var(--grey-text)}
.dev-btn{left:80px;top:1635px}
.photo-room{left:730px;top:1410px;width:330px;height:250px;background:linear-gradient(160deg,#f4f2ee,#d9cbb2 70%,#b88f5f);box-shadow:0 4px 14px rgba(0,0,0,.25)}

/* counties */
.counties{left:0;top:1742px;width:1200px;height:238px;display:flex}
.county{flex:1;display:flex;align-items:center;justify-content:center;color:var(--white);font-size:38px;font-weight:600;letter-spacing:1px}
.county:nth-child(1){background:linear-gradient(180deg,#3a4142,#262b2c)}
.county:nth-child(2){background:linear-gradient(180deg,#2e3536,#1f2425)}
.county:nth-child(3){background:linear-gradient(180deg,#343b3c,#232829)}
.county:nth-child(4){background:linear-gradient(180deg,#2b3132,#202425)}
.county:nth-child(5){background:linear-gradient(180deg,#3c4344,#272c2d)}

/* design grid */
.design-grid{left:300px;top:2018px;width:600px;height:382px;display:grid;grid-template-columns:1fr 1fr;grid-template-rows:1fr 1fr;gap:4px}
.tile-photo-a{background:linear-gradient(150deg,#e9e4dc,#a88a6c)}
.tile-photo-b{background:linear-gradient(150deg,#f0ebe3,#b8936c)}
.tile-text{background:var(--mint);padding:28px 22px}
.tile-text h4{font-size:14px;font-weight:700;letter-spacing:1px;line-height:1.2}
.tile-text h4 span{display:block;color:var(--accent);font-weight:600}
.tile-text .tile-rule{width:120px;height:2px;background:var(--ink);margin:6px 0 8px}
.tile-text p{font-size:10px;line-height:1.4;color:var(--grey-text)}

/* footer */
.site-footer{left:0;top:2448px;width:1200px;height:296px;background:var(--darker);color:var(--white)}
.footer-brand{left:70px;top:90px;display:flex;flex-direction:column;align-items:center;gap:14px}
.footer-brand .brand-mark{width:70px;height:70px;border:3px solid #8fb3b0}
.footer-brand .brand-name{font-size:22px}
.about-title{left:400px;top:82px;font-size:30px;font-weight:600;letter-spacing:2px}
.about-copy{left:400px;top:140px;width:360px;font-size:16px;line-height:1.35;font-weight:600}
.contact-list{left:795px;top:70px;list-style:none}
.contact-list li{display:flex;align-items:center;gap:16px;font-size:18px;margin-bottom:22px}
.contact-list svg{width:26px;height:26px;flex:none}
</style>
</head>
<body>

<section class="abs hero">
  <div class="hero-photo" role="img" aria-label="Bright modern white kitchen interior with faceted geometric wall"></div>
  <div class="hero-fade"></div>
  <header class="site-header">
    <a class="nav-link" href="#">HOME</a>
    <a class="nav-link" href="#">PROJECTS</a>
    <div class="brand"><span class="brand-mark"></span><span class="brand-name">Quartz Oak</span></div>
    <a class="nav-link" href="#">ABOUT</a>
    <a class="nav-link" href="#">CONTACT</a>
  </header>
  <h1 class="abs hero-title">Redesign Your<strong>PROPERTY</strong></h1>
  <p class="abs hero-copy">At Quartz Oak we develop beautiful and unique properties in and around South London. We strive for perfection and never stop changing ourselves</p>
  <span class="btn">View More</span>
</section>

<section class="abs services">
  <div class="service">
    <svg viewBox="0 0 130 130" fill="none" stroke="#1f2324" stroke-width="6" stroke-linejoin="round">
      <path d="M65 20 L115 45 L65 70 L15 45 Z"/>
      <path d="M15 62 L65 87 L115 62"/>
      <path d="M15 80 L65 105 L115 80"/>
    </svg>
    <h3>PROPERTY SPACE<br>PLANNING</h3>
  </div>
  <div class="service">
    <svg viewBox="0 0 130 130" fill="none" stroke="#1f2324" stroke-width="6" stroke-linejoin="round">
      <rect x="28" y="14" width="74" height="96"/>
      <path d="M40 34h50M40 50h50M40 66h30"/>
      <path d="M60 110 L100 78 L112 90 L72 120 L58 122 Z" fill="#1f2324"/>
    </svg>
    <h3>PROPERTY REDESIGN<br>SERVICES</h3>
  </div>
  <div class="service">
    <svg viewBox="0 0 130 130" fill="none" stroke="#1f2324" stroke-width="6" stroke-linecap="round">
      <path d="M42 80 C22 62 28 22 62 20 C88 20 98 50 82 74 C78 80 76 86 76 92 H48 C48 88 46 84 42 80 Z"/>
      <path d="M50 104h26M54 116h18"/>
      <circle cx="98" cy="30" r="10"/>
      <path d="M98 12v6M98 42v6M80 30h6M110 30h6"/>
    </svg>
    <h3>PROPERTY RELOCATION<br>MANAGEMENT</h3>
  </div>
</section>

<div class="abs motive-band"></div>
<div class="photo photo-hall" role="img" aria-label="Warm timber-panelled hallway in a converted Victorian building"></div>
<div class="photo photo-lounge" role="img" aria-label="Lounge with dark green walls and period furniture"></div>
<div class="photo photo-dining" role="img" aria-label="Wood-lined dining room interior"></div>
<h2 class="abs motive-title">OUR BUSINESS MOTIVE</h2>
<div class="abs motive-rule"></div>
<p class="abs motive-copy">we work to regenerate buildings to create new employment opportunities, housing, and revive the town Centre Target Market(s) like</p>

<h2 class="abs dev-title">PROPERTY DEVELOPERS IN<br><span>SOUTH (East of London)</span></h2>
<div class="abs dev-rule"></div>
<p class="abs dev-copy">We've been developing properties in and around South London for the last 4 years. We are a small team of dedicated professionals and we ensure that our exacting standards are met throughout the whole design and build process.</p>
<span class="abs btn dev-btn">View More</span>
<div class="abs photo-room" role="img" aria-label="Light open-plan living room with wooden floor and large windows"></div>

<section class="abs counties">
  <div class="county" role="img" aria-label="Kent houses at dusk">Kent</div>
  <div class="county" role="img" aria-label="Surrey street scene">Surrey</div>
  <div class="county" role="img" aria-label="Sussex cottages">Sussex</div>
  <div class="county" role="img" aria-label="Dorset homes">Dorset</div>
  <div class="county" role="img" aria-label="Hampshire house at night">Hampshire</div>
</section>

<section class="abs design-grid">
  <div class="tile-photo-a" role="img" aria-label="Interior of a converted living space with sofa and timber ceiling"></div>
  <div class="tile-text">
    <h4>INTERIOR<span>DESIGN</span></h4>
    <div class="tile-rule"></div>
    <p>We've been developing properties in and around South London for the last 4 years. We are a small team of dedicated professionals.</p>
  </div>
  <div class="tile-text">
    <h4>STRUCTURE<span>DESIGN</span></h4>
    <div class="tile-rule"></div>
    <p>We've been developing properties in and around South London for the last 4 years. We are a small team of dedicated professionals.</p>
  </div>
  <div class="tile-photo-b" role="img" aria-label="Bright converted interior with exposed beams"></div>
</section>

<footer class="abs site-footer">
  <div class="abs footer-brand"><span class="brand-mark"></span><span class="brand-name">Quartz Oak</span></div>
  <h2 class="abs about-title">ABOUT US</h2>
  <p class="abs about-copy">We are property developers in Kent (south east of London) who want to see the local town change.</p>
  <ul class="abs contact-list">
    <li><svg viewBox="0 0 26 26" fill="none" stroke="#fff" stroke-width="2"><rect x="2" y="5" width="22" height="16"/><path d="M2 5l11 9 11-9"/></svg>hello@quartzoak.co.uk</li>
    <li><svg viewBox="0 0 26 26" fill="#fff"><path d="M13 1C8 1 4 5 4 10c0 7 9 15 9 15s9-8 9-15c0-5-4-9-9-9zm0 13a4 4 0 110-8 4 4 0 010 8z"/></svg>12 Elm Street, Ashford Road</li>
    <li><svg viewBox="0 0 26 26" fill="#fff"><path d="M6 2l5 5-3 3c1 3 4 6 7 7l3-3 5 5-3 4C10 23 3 16 2 5z"/></svg>01632 960481</li>
  </ul>
</footer>

</body>
</html>
```